Greek Yogurt Design

Design Brief – Premium Greek Yogurt Line (150g Pot)
Background
We are a small-to-medium dairy producer launching a new premium Greek yogurt range. This line will come in slightly larger pots than our standard yogurts, and we are targeting an upmarket clientele with a higher price point.
Product Details
Product: Greek Yogurt (fruit on the bottom, yogurt on top)
Flavours:
Natural
Strawberry
Forest Fruit
Peach & Apricot
Vanilla
Mango
Weight: 150g
Kosher Certification: 2 logos must be applied neatly (logos provided).
Lid: Standard universal lid (not flavour-specific).
Design Style
Clean, elegant, and premium feel (avoid clutter).
Should stand out as sophisticated compared to our standard range.
Visual hierarchy:
Brand & product type (Greek Yogurt) should be clear.
Flavour indicated with subtle but distinct cues (colour palette, fruit illustration/photography).
“Fruit on the bottom” message should be communicated simply.
Premium cues: minimalist typography, restrained colour palette, elegant fruit imagery.
References / Inspiration
Velmora Yogurt
– clean, bold, dairy-traditional.
Brask Dairy Greek Style
– natural, elegant design.
Lunaro Greek Yogurt
– modern, colourful yet clean.
Deliverables
Pot sleeve / pot design (to wrap around container).
Must work across all flavours with colour/flavour variation.
Space for universal lid (do not design individual lids).
Application of 2 kosher logos in a balanced way.
Updates
Industry/Entity Type
Dairy
Colors
Designer to choose colors to be used in the design.
Look and feel
Each slider illustrates characteristics of the customer's brand and the style your logo design should communicate.

```html
<!DOCTYPE html>
<html lang="en">
<head>
<meta charset="utf-8">
<title>Greek Yogurt – Pot Sleeves</title>
<link rel="stylesheet" href="https://fonts.googleapis.com/css2?family=Kaushan+Script&family=Tinos:wght@400;700&display=swap">
<style>
  :root {
    --bg-center: #7a7a7a;
    --bg-edge: #4e4e4e;
    --sleeve-white: #fbfbfb;
    --ink: #1c1c1c;
    --brand-green: #5bbb46;
    --vanilla: #ebe35a;
    --vanilla-dark: #d9cf3c;
    --strawberry: #e67ab2;
    --strawberry-dark: #d65c9c;
    --badge-line: #2b2b2b;
    --badge-green: #3aa047;
  }
  * { box-sizing: border-box; margin: 0; padding: 0; }
  html, body { width: 1200px; height: 735px; overflow: hidden; }
  body {
    background: radial-gradient(ellipse at 50% 45%, var(--bg-center) 0%, var(--bg-edge) 80%);
    position: relative;
  }
  .sleeve {
    position: absolute;
    top: 215px;
    width: 500px;
    height: 330px;
    background: var(--sleeve-white);
    border-radius: 6px;
    overflow: hidden;
    box-shadow: 0 8px 24px rgba(0,0,0,.25);
  }
  .sleeve--vanilla { left: 65px; --flavour: var(--vanilla); --flavour-dark: var(--vanilla-dark); }
  .sleeve--strawberry { left: 635px; --flavour: var(--strawberry); --flavour-dark: var(--strawberry-dark); }
  .sleeve__rim {
    position: absolute; left: 0; top: 0; right: 0; height: 52px;
    background: linear-gradient(180deg, var(--flavour) 0%, var(--flavour-dark) 100%);
  }
  .sleeve__flavour-band {
    position: absolute; right: 22px; top: 52px; bottom: 0; width: 48px;
    background: var(--flavour);
    display: flex; align-items: center; justify-content: center;
  }
  .sleeve__flavour-name {
    font-family: "Tinos", serif;
    font-size: 30px;
    letter-spacing: 1px;
    color: var(--ink);
    transform: rotate(-90deg);
    white-space: nowrap;
  }
  .brand {
    position: absolute; left: 90px; top: 66px; width: 200px;
    display: flex; align-items: center; justify-content: center; gap: 8px;
  }
  .brand__dot { width: 14px; height: 14px; border-radius: 50%; background: var(--brand-green); }
  .brand__name {
    font-family: "Kaushan Script", cursive;
    font-size: 34px;
    color: var(--brand-green);
  }
  .product-type {
    position: absolute; left: 38px; top: 112px;
    font-family: "Kaushan Script", cursive;
    font-size: 56px;
    color: var(--ink);
    white-space: nowrap;
  }
  .weight {
    position: absolute; left: 44px; top: 262px;
    font-family: "Tinos", serif;
    font-weight: 700;
    font-size: 24px;
    color: var(--ink);
  }
  .flavour-image {
    position: absolute; left: 140px; top: 200px; width: 170px; height: 100px;
    border-radius: 50%;
  }
  .sleeve--vanilla .flavour-image {
    background: radial-gradient(ellipse at 55% 45%, #f2dc4a 0%, #e8d150 30%, #4a3428 60%, rgba(74,52,40,0) 75%);
  }
  .sleeve--strawberry .flavour-image {
    background: radial-gradient(ellipse at 50% 55%, #d8262c 0%, #c91f27 40%, #3f7a3a 62%, rgba(63,122,58,0) 76%);
  }
  .kosher-badges {
    position: absolute; left: 320px; top: 248px;
  }
</style>
</head>
<body>

<section class="sleeve sleeve--vanilla">
  <div class="sleeve__rim"></div>
  <div class="brand"><span class="brand__dot"></span><span class="brand__name">Melkora</span></div>
  <h1 class="product-type">Greek Yogurt</h1>
  <div class="flavour-image" role="img" aria-label="Photograph of a yellow vanilla flower with dark vanilla pods"></div>
  <p class="weight">150g</p>
  <svg class="kosher-badges" width="110" height="50" viewBox="0 0 110 50" role="img" aria-label="Two kosher certification badges">
    <circle cx="22" cy="25" r="21" fill="none" stroke="var(--badge-line)" stroke-width="2"/>
    <circle cx="80" cy="25" r="21" fill="none" stroke="var(--badge-green)" stroke-width="2"/>
  </svg>
  <div class="sleeve__flavour-band"><span class="sleeve__flavour-name">VANILLA</span></div>
</section>

<section class="sleeve sleeve--strawberry">
  <div class="sleeve__rim"></div>
  <div class="brand"><span class="brand__dot"></span><span class="brand__name">Melkora</span></div>
  <h1 class="product-type">Greek Yogurt</h1>
  <div class="flavour-image" role="img" aria-label="Photograph of two ripe red strawberries with green leaves"></div>
  <p class="weight">150g</p>
  <svg class="kosher-badges" width="110" height="50" viewBox="0 0 110 50" role="img" aria-label="Two kosher certification badges">
    <circle cx="22" cy="25" r="21" fill="none" stroke="var(--badge-line)" stroke-width="2"/>
    <circle cx="80" cy="25" r="21" fill="none" stroke="var(--badge-green)" stroke-width="2"/>
  </svg>
  <div class="sleeve__flavour-band"><span class="sleeve__flavour-name">STRAWBERRY</span></div>
</section>

</body>
</html>
```